Rota sem falha

We need a web design for a new company based in João Pessoa, Brazil, called Rota Sem Falha (Smooth Route). After the client/consumer fullfill a questionary about the wanted destination, personal interests and available budget for the trip, we aim to plan a personalized travel guide for that independent travellers, containing informations about the places we suggest them to visit, amount of days indicated in each city, possibles restaurants and hotels. The site will help people to manage their budgets and optimize the time at their travel at a low cost and in a simple way. We would like to see clean and sophisticated design that use colors in shades of black, grey and white (and perhaps a touch of pink - what do you think?). The final design should communicate safety, professionalism and experience.
Updates
Target Market(s)
People who dont like to buy excursion packages but think they could need a consultance in planning their trip
Industry/Entity Type
It Company
Requirements
Must have
- The menu shall indicate the following points (that will lead to new pages):
1-Our Services
2-Prices
2- FAQ
3-Hire a travel expert to plan your trip!
4-Around the world - blog
Fell free to put the logo of the site "Rota Sem Falha" in the top middle/top left/ or wherever you find it is more appropriate.
On the top right we should put a login/register button.
Above that menu, I thought about illustrating with a figure demonstrating how it works - step by step, as seen in the link http://trekvolo.example/ - but in a more clean design.
Nice to have
- Quik coin will be used as the payment option.

```html
<!DOCTYPE html>
<html lang="en">
<head>
<meta charset="utf-8">
<title>Rota Sem Falha – Personalized Travel Guide</title>
<link rel="stylesheet" href="https://fonts.googleapis.com/css2?family=Comfortaa:wght@400;700&family=Russo+One&family=Arimo:wght@400;700&display=swap">
<style>
:root{
  --ink:#111;
  --header-top:#3a3a3a;
  --header-bottom:#050505;
  --sky:#2eb4ee;
  --sky-deep:#1d86d8;
  --lime:#b5d264;
  --card:#2b2b2b;
  --orange:#f7941d;
  --orange-light:#ffc04a;
  --cyan:#1ea7e0;
  --text-grey:#6d6d6d;
  --paper:#efefef;
  --footer:#262626;
}
*{box-sizing:border-box;margin:0;padding:0}
html,body{width:988px;height:1200px;overflow:hidden;background:#fff}
body{position:relative;font-family:"Arimo",Arial,sans-serif;color:var(--ink)}
.abs{position:absolute}

/* header */
.site-header{left:0;top:0;width:988px;height:68px;background:linear-gradient(var(--header-top),var(--header-bottom))}
.header-badge{left:10px;top:24px;width:25px;height:25px;border-radius:50%;background:#fff}
.brand{left:172px;top:12px;font-family:"Comfortaa",sans-serif;font-weight:700;font-size:24px;color:#fff;letter-spacing:.5px;line-height:1.05}
.account{left:730px;top:11px;font-family:"Arimo",sans-serif;font-size:10px;font-weight:700;color:#9a9a9a;letter-spacing:.3px}
.account .sign-in{color:var(--cyan)}
.main-nav{left:370px;top:39px;font-family:"Comfortaa",sans-serif;font-size:13.5px;color:#fff;white-space:nowrap}
.main-nav span.sep{margin:0 8px;color:#ccc}

/* hero */
.hero{left:0;top:68px;width:988px;height:422px;background:radial-gradient(ellipse at 50% 40%,#f3f6f8 0%,#c9dbe4 45%,#7fb2d0 80%,#3f86b8 100%)}
.hero-suitcase{left:150px;top:200px;width:335px;height:290px;background:linear-gradient(135deg,#3a3d44,#15171b);border-radius:26px 26px 0 0}
.hero-title{left:0;top:104px;width:1000px;text-align:center;font-family:"Comfortaa",sans-serif;font-size:39px;line-height:50px;color:#1a1a1a;letter-spacing:.5px}
.hero-arrow{top:256px;width:38px;height:38px}
.hero-arrow.prev{left:12px}
.hero-arrow.next{left:928px}
.budget-art{left:600px;top:345px;width:295px;height:210px;border-radius:18px;background:linear-gradient(150deg,#f2e2b8,#e2c98a 55%,#c9a54a)}

/* how it works band */
.works-band{left:0;top:490px;width:988px;height:128px;background:linear-gradient(var(--sky),var(--sky-deep))}
.tagline{left:165px;top:505px;font-family:"Comfortaa",sans-serif;font-size:14.5px;color:#10243a}
.works-title{left:165px;top:527px;font-family:"Russo One",sans-serif;font-size:27px;color:#111;letter-spacing:.5px}

.step{top:567px;width:137px;height:192px}
.step-top{position:absolute;left:0;top:0;width:137px;height:142px;background:repeating-linear-gradient(45deg,#2f2f2f 0 2px,var(--card) 2px 4px)}
.step-name{position:absolute;left:0;top:6px;width:137px;text-align:center;font-family:"Comfortaa",sans-serif;font-size:19px;color:#fff}
.step-sub{position:absolute;left:0;top:29px;width:137px;text-align:center;font-size:8px;color:#d6d6d6}
.step-num{position:absolute;right:-3px;top:8px;width:17px;height:17px;background:var(--lime);color:#111;font-family:"Russo One",sans-serif;font-size:12px;text-align:center;line-height:17px}
.step-art{position:absolute;left:20px;top:50px;width:97px;height:72px;border-radius:6px}
.step-note{position:absolute;left:0;top:142px;width:137px;height:50px;background:var(--lime);font-size:8px;line-height:15px;color:#2b2b2b;text-align:center;padding:6px 8px 0}

.subscribe-now{left:391px;top:776px;width:206px;height:37px;border-radius:5px;background:linear-gradient(var(--orange-light),var(--orange));border:1px solid #e07a10;font-family:"Russo One",sans-serif;font-size:17px;color:#5a2a00;text-align:center;line-height:35px}

/* about */
.about{left:0;top:826px;width:988px;height:245px;background:linear-gradient(#f7f7f7,#dedede)}
.about h2{position:absolute;font-family:"Comfortaa",sans-serif;font-weight:400;font-size:19px;color:#1a1a1a}
.about-copy{left:158px;top:886px;width:416px;font-size:8.3px;line-height:16.8px;color:var(--text-grey)}
.about-copy p+p{margin-top:6px}
.video{left:609px;top:888px;width:232px;height:137px;background:radial-gradient(#4a4a4a,#1e1e1e)}
.play{left:689px;top:933px;width:74px;height:50px;border-radius:9px;background:#0c0c0c}

/* footer */
.site-footer{left:0;top:1071px;width:988px;height:129px;background:var(--footer)}
.footer-links{top:1095px;font-size:9px;line-height:15.3px;color:#ddd}
.social{top:1095px;width:11px;height:11px;border-radius:50%;background:#8a8a8a}
.copyright{left:389px;top:1125px;width:200px;text-align:center;font-size:9px;color:#ddd}
.footer-brand{left:689px;top:1097px;font-family:"Comfortaa",sans-serif;font-weight:700;font-size:24px;color:#fff;line-height:1.05}
</style>
</head>
<body>

<header class="abs site-header"></header>
<div class="abs header-badge"></div>
<div class="abs brand">ROTA<br>SEM FALHA</div>
<div class="abs account"><span class="sign-in">SIGN IN</span> &nbsp;| &nbsp;REGISTER</div>
<nav class="abs main-nav">Home<span class="sep">//</span>Our Services<span class="sep">//</span>Prices<span class="sep">//</span>FAQ<span class="sep">//</span>Hire a travel expert<span class="sep">//</span>Blog</nav>

<section class="abs hero" role="img" aria-label="World map of the South Atlantic seen in perspective"></section>
<div class="abs hero-suitcase" role="img" aria-label="Black vintage suitcase covered in travel stickers"></div>
<h1 class="abs hero-title">PERSONALIZED TRAVEL GUIDE FOR<br>INDEPENDENT TRAVELLERS</h1>
<svg class="abs hero-arrow prev" viewBox="0 0 38 38"><circle cx="19" cy="19" r="17" fill="rgba(0,0,0,.25)" stroke="#fff" stroke-width="2.5"/><path d="M22 11l-8 8 8 8" fill="none" stroke="#fff" stroke-width="3"/></svg>
<svg class="abs hero-arrow next" viewBox="0 0 38 38"><circle cx="19" cy="19" r="17" fill="rgba(0,0,0,.25)" stroke="#fff" stroke-width="2.5"/><path d="M16 11l8 8-8 8" fill="none" stroke="#fff" stroke-width="3"/></svg>

<section class="abs works-band"></section>
<div class="abs budget-art" role="img" aria-label="Stacked cream suitcases with plane tickets, gold coins and a calculator"></div>
<p class="abs tagline">Generates Your Free Personalized Ready-To-Use Itinerary In Split Seconds.</p>
<h2 class="abs works-title">HOW IT WORKS!</h2>

<div class="abs step" style="left:141px">
  <div class="step-top"></div>
  <div class="step-name">Generate</div><div class="step-sub">your personal trip plan</div>
  <div class="step-num">1</div>
  <div class="step-art" role="img" aria-label="Orange subscribe button with a cursor" style="background:linear-gradient(#ffc04a,#f7941d)"></div>
  <div class="step-note">Simply click the get started button and follow the wizard</div>
</div>
<div class="abs step" style="left:283px">
  <div class="step-top"></div>
  <div class="step-name">Review</div><div class="step-sub">the suggested itinerary</div>
  <div class="step-num">2</div>
  <div class="step-art" role="img" aria-label="Folded map with location pins" style="background:linear-gradient(90deg,#3aa0d8,#6cc7e8,#3aa0d8)"></div>
  <div class="step-note">Attractions, places to eat, hotel, schedule and even directions</div>
</div>
<div class="abs step" style="left:425px">
  <div class="step-top"></div>
  <div class="step-name">Refine</div><div class="step-sub">just about everything</div>
  <div class="step-num">3</div>
  <div class="step-art" role="img" aria-label="Colourful map with hotel, shop and restaurant pins" style="background:linear-gradient(135deg,#49b7e0,#f0d24a,#7cc35a)"></div>
  <div class="step-note">For each change, your trip will be optimized to fit your every whim!</div>
</div>
<div class="abs step" style="left:567px">
  <div class="step-top"></div>
  <div class="step-name">Compare</div><div class="step-sub">just about everything</div>
  <div class="step-num">4</div>
  <div class="step-art" role="img" aria-label="Balance scale holding stacks of gold coins" style="background:linear-gradient(#e0b640,#8f8f8f)"></div>
  <div class="step-note">Find your hotel, and we'll link you to the supplier of your choice</div>
</div>
<div class="abs step" style="left:709px">
  <div class="step-top"></div>
  <div class="step-name">Print</div><div class="step-sub">your plan and bon voyage</div>
  <div class="step-num">5</div>
  <div class="step-art" role="img" aria-label="Printer printing a page" style="background:linear-gradient(#f4f4f4,#9a9a9a)"></div>
  <div class="step-note">After all, travel advice this great shouldn't be left at home!</div>
</div>

<div class="abs subscribe-now">SUBSCRIBE NOW!</div>

<section class="abs about"></section>
<h2 class="abs" style="left:158px;top:852px;font-family:'Comfortaa',sans-serif;font-weight:400;font-size:19px;color:#1a1a1a">ROTA SEM FALHA</h2>
<div class="abs about-copy">
  <p>Lorem ipsum dolor sit amet, consectetuer adipiscing elit, sed diam nonummy nibh euismod tincidunt ut laoreet dolore magna aliquam erat volutpat. Ut wisi enim ad minim veniam, quis nostrud exerci tation ullamcorper suscipit lobortis nisl ut aliquip ex ea commodo consequat. Duis autem vel eum iriure dolor in hendrerit in vulputate velit esse molestie consequat, vel illum dolore eu feugiat nulla facilisis at vero eros et accumsan et iusto odio dignissim qui blandit praesent luptatum zzril delenit augue duis dolore te feugait nulla facilisi.</p>
  <p>Lorem ipsum dolor sit amet, consectetuer adipiscing elit, sed diam nonummy nibh euismod tincidunt ut laoreet dolore magna aliquam erat volutpat. Ut wisi enim ad minim veniam.</p>
</div>
<h2 class="abs" style="left:609px;top:852px;font-family:'Comfortaa',sans-serif;font-weight:400;font-size:17px;color:#1a1a1a">WHAT IS ROTA SEM FALHA?</h2>
<div class="abs video" role="img" aria-label="Introductory video preview"></div>
<div class="abs play"></div>
<svg class="abs" style="left:716px;top:946px" width="22" height="24" viewBox="0 0 22 24"><path d="M0 0l22 12L0 24z" fill="#fff"/></svg>

<footer class="abs site-footer"></footer>
<div class="abs footer-links" style="left:169px">About<br>Advertise<br>Blogs</div>
<div class="abs footer-links" style="left:233px">Legal<br>Jobs<br>Sitemap</div>
<div class="abs social" style="left:467px"></div>
<div class="abs social" style="left:485px"></div>
<div class="abs social" style="left:503px"></div>
<div class="abs copyright">© 2013 Rotasemfalha.example</div>
<div class="abs footer-brand">ROTA<br>SEM FALHA</div>

</body>
</html>
```